Business Cards for Branding (Advertising) Agency

We need stylish and cool business cards.
Additional info:
1) Logo - see the attachment. You can use either the three penguins or just one penguin face (square or round) - at your discretion.
2) Text and other stuff for business card:
front side:
-Logo and company name: company name - Coastal Herons - should be in English as is in logo. This is the only exception. The rest of the text will be in Russian.
-Who we are: Брендинговое агентство
-First and last name:
-Position: Управляющий партнёр
-Address:
-Phone:
-Email:
-Website:
Note: please don't use names of information fields, such as: who we are, first and last name, position, address, phone, email and website.

3) Our suggestions on design:
-The backside of the business card can be either blank or has something on it - at your discretion.
-The business card background should be either white or grey (you can use any tone of grey).

Additional Information:
1) БРЕНДИНГОВОЕ АГЕНТСТВО
2) ул. Вересковая - these two words should be together on the same line
3) тел.: +7 (495) 381-62-09
моб.: +7 (916) 740-28-51

Reason: We would like to receive more stylish designs.

```html
<!DOCTYPE html>
<html lang="ru">
<head>
<meta charset="utf-8">
<title>Coastal Herons — визитные карточки</title>
<link href="https://fonts.googleapis.com/css2?family=Open+Sans:wght@300;400;600;700&family=Josefin+Sans:wght@400&display=swap" rel="stylesheet">
<style>
  :root {
    --bg: #e4e2df;
    --card: #ffffff;
    --orange: #f0a01a;
    --orange-text: #f39a12;
    --ink: #1a1a1a;
    --grey: #555555;
    --grey-light: #8a8a8a;
    --rule: #cfcfcf;
    --art-dark: #1c1c1c;
    --art-mid: #6f6f6f;
  }
  * { box-sizing: border-box; margin: 0; padding: 0; }
  html, body { width: 1200px; height: 1000px; overflow: hidden; }
  body {
    background: var(--bg);
    font-family: "Open Sans", Arial, sans-serif;
    position: relative;
  }
  .card {
    position: absolute;
    top: 200px;
    width: 350px;
    height: 600px;
    background: var(--card);
    border-radius: 18px;
    box-shadow: 0 6px 18px rgba(0,0,0,0.14);
    overflow: hidden;
  }
  .card--logo { left: 200px; }
  .card--contact { left: 650px; }

  /* Logo side */
  .logo-art {
    position: absolute;
    left: 95px; top: 150px;
    width: 200px; height: 210px;
    border-radius: 40px;
    background: linear-gradient(160deg, var(--art-mid), var(--art-dark));
  }
  .brand-name {
    position: absolute;
    left: 0; right: 0; top: 385px;
    text-align: center;
    font-family: "Josefin Sans", Arial, sans-serif;
    font-weight: 400;
    font-size: 34px;
    letter-spacing: 5px;
    color: var(--ink);
  }
  .brand-name .dot {
    display: inline-block;
    width: 10px; height: 10px;
    border-radius: 50%;
    background: var(--ink);
    margin-left: 8px;
    vertical-align: middle;
  }

  /* Contact side */
  .contact-top { position: absolute; left: 38px; right: 30px; top: 42px; }
  .person-name { font-size: 22px; font-weight: 700; color: var(--orange-text); }
  .person-role { font-size: 16px; font-weight: 600; color: var(--grey); margin-top: 2px; }
  .divider { border-top: 2px dotted var(--rule); margin: 16px 0 14px; }
  .contact-list { list-style: none; font-size: 15px; font-weight: 300; color: var(--grey-light); line-height: 1.55; }
  .contact-list li { display: flex; align-items: center; gap: 10px; }
  .contact-list svg { width: 13px; height: 13px; flex: none; }

  .band {
    position: absolute;
    left: 0; right: 0; bottom: 0;
    height: 260px;
    background: var(--orange);
  }
  .band-art {
    position: absolute;
    right: 22px; bottom: 190px;
    width: 120px; height: 130px;
    border-radius: 26px;
    background: linear-gradient(160deg, var(--art-mid), var(--art-dark));
  }
  .band-text { position: absolute; left: 38px; right: 30px; top: 70px; color: #ffffff; }
  .band-brand {
    font-family: "Josefin Sans", Arial, sans-serif;
    font-size: 22px;
    letter-spacing: 3px;
    color: var(--ink);
    margin-bottom: 14px;
  }
  .agency { font-size: 17px; font-weight: 700; }
  .address { font-size: 15px; font-weight: 400; line-height: 1.45; margin-top: 4px; }
</style>
</head>
<body>

<section class="card card--logo">
  <div class="logo-art" role="img" aria-label="Brand mascot illustration"></div>
  <div class="brand-name">COASTAL HERONS<span class="dot"></span></div>
</section>

<section class="card card--contact">
  <div class="contact-top">
    <div class="person-name">Мария Лебедева</div>
    <div class="person-role">Управляющий партнёр</div>
    <div class="divider"></div>
    <ul class="contact-list">
      <li>
        <svg viewBox="0 0 16 16"><path fill="#f0a01a" d="M3 1l3 3-2 2c1 2 3 4 5 5l2-2 3 3-2 3C7 15 1 9 1 3z"/></svg>
        +7 (916) 740-28-51
      </li>
      <li>
        <svg viewBox="0 0 16 16"><rect x="1" y="3" width="14" height="10" fill="#f0a01a"/><path d="M1 3l7 6 7-6" fill="none" stroke="#fff" stroke-width="1.4"/></svg>
        maria@coastalherons.ru
      </li>
      <li>
        <svg viewBox="0 0 16 16"><circle cx="3" cy="13" r="2" fill="#f0a01a"/><path d="M2 7a7 7 0 0 1 7 7M2 2a12 12 0 0 1 12 12" fill="none" stroke="#f0a01a" stroke-width="2"/></svg>
        www.coastalherons.ru
      </li>
    </ul>
  </div>

  <div class="band">
    <div class="band-text">
      <div class="band-brand">COASTAL HERONS</div>
      <div class="agency">Брендинговое агентство</div>
      <div class="address">119072, г. Москва<br>ул. Вересковая, д.12, стр.5</div>
    </div>
  </div>
  <div class="band-art" role="img" aria-label="Brand mascot illustration"></div>
</section>

</body>
</html>
```